Tandel Marketing needs a new website design

We need a homepage and sub-page design for our new marketing consulting business based in Perth, Western Australia. www.tandelmarketing-example.com.au

About Us:

Tandel Marketing specialises in providing professional and result orientated marketing advice to small and medium sized business. We focus on client's overall marketing communication mix and analyse their current marketing activities and give advise where to invest their budget in the future.

We also function as marketing freelancers and can put the developed marketing plans and strategies into action.

Colour Suggestions based on newly designed logo:
orange, dark blue, black and white

The final design should reflect strategic solutions, success, trust & knowledge.

Please refer to attached documents:
Wireframe - for an indication of the sections needed on the site
Sitemap - as guidance how the content is arranged/interlinked
Services - overview of our marketing consulting service areas
Logo - use as guideline for colours and style

Industry websites that are different and that we like:

1. http://www.vorlinqa-example.com/index.htm
- like the simplicity of this site

2. http://www.plaxterwood-example.com/ - like the integration of the services into the header

3. http://www.gorumisa-example.com/
like the concept of the display of services - can you come up with something for us based on our overview of services

Target Market(s)

Marketing Managers & Business Owners (age 30-50) of small to medium sized businesses in Perth/ Western Australia

Industry/Entity Type

Marketing

Requirements
Must have
• - clean design and customised site
- all elements as specified in the wireframes document (provided a few options but open to suggestions and ideas
- looking for ideas to display our services as per overview page which can be integrated into each page of the website
Should not have
• don’t want a template looking site
please don't just copy our wireframes and make the site too boxy

```html
<!DOCTYPE html>
<html lang="en">
<head>
<meta charset="utf-8">
<title>Tandel Marketing</title>
<link href="https://fonts.googleapis.com/css2?family=Arimo:wght@400;700&family=Questrial&display=swap" rel="stylesheet">
<style>
:root{
  --orange:#f7780f;
  --orange-dark:#e05f00;
  --blue:#1f3a9c;
  --blue-deep:#17308a;
  --white:#ffffff;
  --ink:#2b2b2b;
  --panel:#e6e6e6;
  --nav-top:#b9b9b9;
  --nav-bottom:#8e8e8e;
  --footer:#45474c;
  --footer-text:#e3e3e3;
}
*{margin:0;padding:0;box-sizing:border-box}
html,body{width:1200px;height:1021px;overflow:hidden;background:var(--white)}
body{position:relative;font-family:"Arimo",Arial,sans-serif;color:var(--ink)}

.brand{position:absolute;left:52px;top:50px;display:flex;align-items:center;gap:14px}
.brand-dot{width:86px;height:86px;border-radius:50%;background:var(--orange)}
.brand-name{font-family:"Questrial",sans-serif;font-size:38px;line-height:1;color:var(--orange);letter-spacing:1px}

.main-nav{position:absolute;left:33px;top:173px;width:980px;height:33px;
  background:linear-gradient(var(--nav-top),var(--nav-bottom));border-radius:5px 5px 0 0}
.main-nav a{position:absolute;top:8px;color:var(--white);font-size:17px;text-decoration:none;white-space:nowrap}

.hero{position:absolute;left:0;top:205px;width:1200px;height:356px;
  background:radial-gradient(ellipse at 40% 45%,#2545ad 0%,var(--blue) 55%,var(--blue-deep) 100%)}
.hero-title{position:absolute;left:76px;top:84px;font-size:86px;font-weight:700;color:var(--white);
  letter-spacing:-2px;text-shadow:5px 4px 0 #3d6ee0}
.hero-lead{position:absolute;left:85px;top:194px;font-size:18px;line-height:23px;color:var(--white)}
.cta{position:absolute;left:727px;top:38px;width:225px;height:50px;border-radius:4px;
  background:linear-gradient(#ff8a1f,var(--orange-dark));color:var(--white);font-size:25px;
  letter-spacing:-1px;line-height:50px;text-align:center;text-shadow:1px 1px 2px rgba(0,0,0,.45);
  box-shadow:0 2px 4px rgba(0,0,0,.35)}
.route-map{position:absolute;left:523px;top:128px;width:612px;height:222px;border-radius:6px;
  background:linear-gradient(180deg,rgba(247,120,15,.18),rgba(247,120,15,.32) 50%,rgba(255,255,255,.10))}

.intro{position:absolute;left:57px;top:626px;width:512px;font-size:16.4px;line-height:28.3px}

.side-panel{position:absolute;left:590px;width:526px;background:var(--panel)}
.panel-title{position:absolute;left:12px;font-size:34px;font-weight:400;color:var(--orange)}
.news{top:584px;height:93px}
.news .panel-title{top:4px}
.news-date{position:absolute;left:129px;top:14px;font-size:12.5px}
.news-text{position:absolute;left:129px;top:48px;width:380px;font-size:12.5px;line-height:17px}
.clients{top:690px;height:110px}
.clients .panel-title{top:4px}
.client-list{position:absolute;left:112px;top:62px;display:flex;gap:18px;align-items:center}
.client{display:flex;align-items:center;gap:5px;font-size:13px;color:#555}
.client-mark{width:10px;height:10px;border-radius:50%;background:#8a8a8a}

.site-footer{position:absolute;left:0;top:874px;width:1200px;height:147px;background:var(--footer);
  color:var(--footer-text);text-align:center}
.footer-links{position:absolute;top:31px;width:100%;font-size:14.5px}
.footer-links span{margin:0 14px}
.copyright{position:absolute;top:62px;width:100%;font-size:13px}
</style>
</head>
<body>

<header class="brand">
  <div class="brand-dot"></div>
  <div class="brand-name">Tandel Marketing</div>
</header>

<nav class="main-nav">
  <a style="left:26px">Home</a>
  <a style="left:121px">Marketing Consulting</a>
  <a style="left:343px">Marketing Services</a>
  <a style="left:536px">Blog</a>
  <a style="left:616px">About Us</a>
  <a style="left:756px">Portfolio</a>
  <a style="left:869px">Contact Us</a>
</nav>

<section class="hero">
  <h1 class="hero-title">Strategy</h1>
  <p class="hero-lead">Improve your marketing strategy now and<br>reap the succesful result.</p>
  <div class="route-map" role="img" aria-label="Route-map illustration of the service path from problem, through consultation, planning, branding and internet marketing, to solution"></div>
  <div class="cta">TALK TO US NOW</div>
</section>

<p class="intro">Tandel Marketing specialises in providing professional and result orientated marketing advice to small and medium sized business. We focus on client's overall marketing communication mix and analyse their current marketing activities and give advise where to invest their budget in the future.</p>

<aside class="side-panel news">
  <h2 class="panel-title">News</h2>
  <div class="news-date">12/05/12</div>
  <p class="news-text">Tandel Marketing has helped Mellowdrop Ice Cream Store with their rebranding materials and new campaign!</p>
</aside>

<aside class="side-panel clients">
  <h2 class="panel-title">Our Clients</h2>
  <div class="client-list">
    <span class="client"><span class="client-mark"></span>Fernwild</span>
    <span class="client">Brightlane</span>
    <span class="client">Marvelle</span>
    <span class="client">Barkly</span>
    <span class="client">Greenmarket</span>
  </div>
</aside>

<footer class="site-footer">
  <div class="footer-links">Tandel Marketing Consulting Perth<span>|</span>Sitemap<span>|</span>Privacy Policy</div>
  <div class="copyright">Copyright © 2012 Tandel Marketing</div>
</footer>

</body>
</html>
```